Letterhead design for Sleep Consulting Business

I'm looking for a new letterhead (heading/footer) design for my Sleep Consulting Business, I work with families to help their children improve their sleep.

The heading/footer will used in Microsoft Word Only-to be used for all of my documents such as writing Sleep Plans. I need to utilize as much working space in the document as possible. This will NOT be printed out on paper- it will only be used for heading/footer on microsoft word, then emailed to clients, who may print it at home.

My brand colors:
Dark Blue Hex: 1F2A42
Lighter Blueish Hex: 90BEC9
You're welcome to check out my website for inspiration- it is freshly created with other colors as well, and I love the outcome. www.hollowpinerest.com

Target Market(s)

Tired parents

Font styles to use
Script
Other font styles liked:
• Great Vibe, Lato or Just Another Hand are all used currently for my brand. Open to other options.

Requirements
Must have
• The letterhead (heading/footer) MUST be kept narrow (height-wise), so I have plenty of space on my document, while including important information.

It should look professional on screen, and when printed.

Must include my business name OR logo (Hollow Pine Sleep Consulting), and my email address. Mara@hollowpinerest.com

Website is optional, not required, just if you need to fill in a spot: www.hollowpinerest.com

```html
<!DOCTYPE html>
<html lang="en">
<head>
<meta charset="utf-8">
<title>Hollow Pine Sleep Consulting – Letterhead</title>
<link rel="stylesheet" href="https://fonts.googleapis.com/css2?family=Great+Vibes&display=swap">
<style>
  :root {
    --navy: #1F2A42;
    --sky: #90BEC9;
    --paper: #FFFFFF;
  }
  html, body {
    margin: 0;
    padding: 0;
    overflow: hidden;
    background: var(--paper);
  }
  .letterhead {
    position: relative;
    width: 938px;
    height: 1200px;
    background: var(--paper);
    overflow: hidden;
  }
  .brand {
    position: absolute;
    top: 46px;
    left: 0;
    width: 100%;
    display: flex;
    justify-content: center;
    align-items: center;
    gap: 20px;
  }
  .brand-dot {
    width: 58px;
    height: 58px;
    border-radius: 50%;
    background: var(--sky);
    flex: none;
  }
  .brand-name {
    font-family: "Great Vibes", cursive;
    font-weight: 400;
    font-size: 44px;
    line-height: 1;
    color: var(--navy);
    white-space: nowrap;
  }
  .footer-rule {
    position: absolute;
    left: 0;
    top: 0;
    width: 938px;
    height: 1200px;
  }
  .contact {
    position: absolute;
    top: 1137px;
    left: 56px;
    display: flex;
    align-items: center;
    gap: 22px;
    font-family: "Great Vibes", cursive;
    font-size: 28px;
    line-height: 1;
    color: var(--navy);
    white-space: nowrap;
  }
  .contact-item {
    display: flex;
    align-items: center;
    gap: 7px;
  }
  .contact-icon {
    width: 17px;
    height: 17px;
    flex: none;
  }
</style>
</head>
<body>
  <main class="letterhead">
    <header class="brand">
      <span class="brand-dot" aria-hidden="true"></span>
      <span class="brand-name">Hollow Pine Sleep Consulting</span>
    </header>

    <svg class="footer-rule" viewBox="0 0 938 1200" aria-hidden="true">
      <path d="M0 1114 H671 Q698 1178 742 1200" fill="none" stroke="var(--sky)" stroke-width="1.2"/>
    </svg>

    <footer class="contact">
      <span class="contact-item">
        <svg class="contact-icon" viewBox="0 0 16 16" aria-hidden="true">
          <circle cx="8" cy="8" r="8" fill="var(--navy)"/>
          <rect x="4" y="5.3" width="8" height="5.4" fill="none" stroke="#fff" stroke-width="1"/>
          <path d="M4 5.5 L8 8.6 L12 5.5" fill="none" stroke="#fff" stroke-width="1"/>
        </svg>
        mara@hollowpinerest.com
      </span>
      <span class="contact-item">
        <svg class="contact-icon" viewBox="0 0 16 16" aria-hidden="true">
          <circle cx="8" cy="8" r="8" fill="var(--navy)"/>
          <circle cx="8" cy="8" r="4.8" fill="none" stroke="#fff" stroke-width="0.9"/>
          <ellipse cx="8" cy="8" rx="2" ry="4.8" fill="none" stroke="#fff" stroke-width="0.9"/>
          <path d="M3.2 8 H12.8 M4 5.6 H12 M4 10.4 H12" stroke="#fff" stroke-width="0.8"/>
        </svg>
        www.hollowpinerest.com
      </span>
    </footer>
  </main>
</body>
</html>
```